Wedding Vows Poster for a Frame (anniversary gift )

I need an 8 X11 copy of both or wedding vows that I can frame in a classy and timeless modern font to frame for our house .

see file attach for text (vows)

project is now close thank you for all your help

Wedding

```html
<!DOCTYPE html>
<html lang="en">
<head>
<meta charset="utf-8">
<title>Our Wedding Vows</title>
<link rel="stylesheet" href="https://fonts.googleapis.com/css2?family=Macondo&display=swap">
<style>
  :root {
    --paper: #ffffff;
    --field: #a8a8a9;
    --ink: #000000;
    --shade: rgba(0, 0, 0, 0.38);
  }
  html, body {
    margin: 0;
    padding: 0;
    width: 927px;
    height: 1200px;
    overflow: hidden;
    background: var(--paper);
  }
  .poster {
    position: relative;
    width: 612px;
    height: 792px;
    transform: scale(1.5152);
    transform-origin: 0 0;
    font-family: "Macondo", cursive;
    color: var(--ink);
  }
  .poster__field {
    position: absolute;
    left: 10px;
    top: 12px;
    width: 593px;
    height: 770px;
    background: var(--field);
  }
  .vow-line {
    position: absolute;
    font-size: 10.4px;
    line-height: 14px;
    white-space: nowrap;
    text-align: justify;
    text-align-last: justify;
    text-shadow: 1px 2px 2px var(--shade);
  }
  .vow-line--left { text-align-last: left; text-align: left; }
  .vow-title {
    position: absolute;
    font-size: 11.5px;
    line-height: 14px;
    text-align: center;
    white-space: nowrap;
    text-shadow: 1px 2px 2px var(--shade);
  }
  .signature-name {
    position: absolute;
    font-size: 26px;
    line-height: 1;
    white-space: nowrap;
    text-shadow: 2px 3px 3px var(--shade);
    transform-origin: 0 50%;
  }
  .signature-name--groom { left: 198px; top: 553px; transform: rotate(50deg); }
  .signature-name--bride { left: 337px; top: 600px; transform: rotate(-40deg); }
  .center-heart {
    position: absolute;
    left: 280px;
    top: 618px;
    width: 56px;
    height: 50px;
    filter: drop-shadow(2px 3px 2px var(--shade));
  }
</style>
</head>
<body>
<main class="poster">
  <div class="poster__field"></div>

  <section class="vows vows--groom">
    <div class="vow-title" style="left:93px;top:200px;width:160px;">Daniel to Claire</div>
    <div class="vow-line" style="left:62px;top:216px;width:168px;">“Three years ago I fell in love</div>
    <div class="vow-line" style="left:50px;top:232px;width:212px;">with you on our journey trough Peru,</div>
    <div class="vow-line" style="left:37px;top:248px;width:267px;">your love for life , your drive, your</div>
    <div class="vow-line" style="left:32px;top:264px;width:273px;">beautiful smile, and natural beauty were at</div>
    <div class="vow-line" style="left:22px;top:280px;width:284px;">the time what got my attention. Now that I</div>
    <div class="vow-line" style="left:22px;top:296px;width:284px;">know much more about you I have realize how</div>
    <div class="vow-line" style="left:22px;top:312px;width:284px;">much more complete of an individual you are.</div>
    <div class="vow-line" style="left:22px;top:328px;width:284px;">For a long time I wish I had meet you before</div>
    <div class="vow-line" style="left:28px;top:344px;width:278px;">however only now I can appreciate you fully.</div>
    <div class="vow-line" style="left:34px;top:360px;width:272px;">I love you Claire. This ring represents my</div>
    <div class="vow-line" style="left:40px;top:376px;width:266px;">commitment to you as your partner and to</div>
    <div class="vow-line" style="left:56px;top:392px;width:250px;">our&nbsp; marriage.&nbsp; As&nbsp; your&nbsp; husband&nbsp; I</div>
    <div class="vow-line" style="left:73px;top:408px;width:233px;">promise to be loyal and give you the</div>
    <div class="vow-line" style="left:90px;top:424px;width:216px;">best that I can, protect and cherish</div>
    <div class="vow-line" style="left:105px;top:440px;width:201px;">you I will always be there for</div>
    <div class="vow-line" style="left:125px;top:456px;width:181px;">you trough good and hard</div>
    <div class="vow-line" style="left:146px;top:472px;width:160px;">time. I will grow old with</div>
    <div class="vow-line" style="left:200px;top:488px;width:106px;">you and love you</div>
    <div class="vow-line" style="left:247px;top:504px;width:59px;">forever.”</div>
  </section>

  <section class="vows vows--bride">
    <div class="vow-title" style="left:355px;top:200px;width:156px;">Claire to Daniel</div>
    <div class="vow-line" style="left:350px;top:216px;width:200px;">“This&nbsp; ring&nbsp; represents&nbsp; my</div>
    <div class="vow-line" style="left:330px;top:232px;width:240px;">commitment&nbsp; to&nbsp; you&nbsp; as&nbsp; your</div>
    <div class="vow-line" style="left:325px;top:248px;width:263px;">partner and to our marriage.&nbsp; As</div>
    <div class="vow-line" style="left:315px;top:264px;width:275px;">your partner I promise to always do</div>
    <div class="vow-line" style="left:315px;top:280px;width:280px;">my best to support, respect, be</div>
    <div class="vow-line" style="left:315px;top:296px;width:282px;">compassionate and loving to you.&nbsp; And</div>
    <div class="vow-line" style="left:315px;top:312px;width:282px;">as your wife, I promise to always to my</div>
    <div class="vow-line" style="left:315px;top:328px;width:282px;">best to be honest, trust worthy trust</div>
    <div class="vow-line" style="left:315px;top:344px;width:280px;">and during challenging times to have</div>
    <div class="vow-line" style="left:315px;top:360px;width:270px;">the faith that we will somehow</div>
    <div class="vow-line" style="left:322px;top:376px;width:248px;">overcome it and be even stronger</div>
    <div class="vow-line vow-line--left" style="left:315px;top:392px;">on the other side. Dani, you are</div>
    <div class="vow-line vow-line--left" style="left:315px;top:408px;">my favorite person, I love you</div>
    <div class="vow-line vow-line--left" style="left:315px;top:424px;">with all my heart and I am so</div>
    <div class="vow-line" style="left:315px;top:440px;width:195px;">very&nbsp; proud&nbsp; to&nbsp; be&nbsp; your</div>
    <div class="vow-line vow-line--left" style="left:315px;top:456px;">wife.”</div>
    <div class="vow-line vow-line--left" style="left:315px;top:472px;">Love always,</div>
  </section>

  <div class="signature-name signature-name--groom">Daniel</div>
  <div class="signature-name signature-name--bride">Claire</div>

  <svg class="center-heart" viewBox="0 0 56 50" aria-hidden="true">
    <path d="M28 48 C20 40 2 30 2 15 C2 6 9 1 16 1 C22 1 26 5 28 9 C30 5 34 1 40 1 C47 1 54 6 54 15 C54 30 36 40 28 48 Z" fill="var(--ink)"/>
  </svg>
</main>
</body>
</html>
```